Geschäftspapiere für Werbe/Media Agentur
Zielgruppe
Werbe/Media Agentur
Aufgabenstellung
Ich brauche das ganze Konzept/Corporate. Visitenkarte, Briefumschläge klein und groß mit und ohne Fenster, Briefbogen usw. was alles mit der Firma zu tun hat. Diese benötige ich in schwarz matt und in weißer Hintergrund.

```html
<!DOCTYPE html>
<html lang="de">
<head>
<meta charset="utf-8">
<title>Velto Studio – Geschäftsausstattung</title>
<link rel="stylesheet" href="https://fonts.googleapis.com/css2?family=Montserrat:wght@400;500;600;700&display=swap">
<style>
  :root {
    --stage: #d6d6d6;
    --paper: #f4f4f2;
    --ink: #2b3540;
    --ink-soft: #5a6068;
    --panel-white: #ffffff;
    --panel-dark: #4b4b4b;
    --card: #707070;
    --card-dark: #5c5c5c;
    --accent-yellow: #e9d21f;
    --r-yellow: #f6e400;
    --r-orange: #f39200;
    --r-red: #e30613;
    --r-magenta: #c0137f;
    --r-purple: #5b2a86;
    --r-blue: #1d71b8;
    --r-green: #3aaa35;
  }
  * { box-sizing: border-box; margin: 0; padding: 0; }
  html, body { width: 1200px; height: 1200px; overflow: hidden; }
  body {
    position: relative;
    background: var(--stage);
    font-family: "Montserrat", sans-serif;
    color: var(--ink);
  }

  .rainbow-band { display: flex; }
  .rainbow-band span { flex: 1; }
  .rainbow-band .y { background: var(--r-yellow); }
  .rainbow-band .o { background: var(--r-orange); }
  .rainbow-band .r { background: var(--r-red); }
  .rainbow-band .m { background: var(--r-magenta); }
  .rainbow-band .p { background: var(--r-purple); }
  .rainbow-band .b { background: var(--r-blue); }
  .rainbow-band .g { background: var(--r-green); }

  /* Letterhead */
  .letterhead {
    position: absolute; left: 356px; top: 28px;
    width: 488px; height: 690px;
    background: var(--paper);
    box-shadow: 0 6px 18px rgba(0,0,0,.18);
    font-size: 6.5px; line-height: 1.55;
  }
  .letterhead .rainbow-band { position: absolute; top: 0; left: 0; right: 0; height: 6px; }
  .letterhead .sender-line { position: absolute; left: 52px; top: 66px; font-size: 5.5px; color: var(--ink-soft); }
  .letterhead .recipient { position: absolute; left: 52px; top: 80px; }
  .brand-mark {
    display: flex; align-items: center; gap: 6px;
    font-weight: 600; color: var(--ink); letter-spacing: .02em;
  }
  .brand-mark .dot { border-radius: 50%; background: var(--ink); }
  .letterhead .brand-mark { position: absolute; right: 44px; top: 66px; font-size: 13px; }
  .letterhead .brand-mark .dot { width: 12px; height: 12px; }
  .letterhead .letter-body { position: absolute; left: 52px; right: 52px; top: 160px; }
  .letterhead .letter-body p { margin-bottom: 8px; }
  .letterhead .closing { margin-top: 14px; }
  .letterhead .signature { margin-top: 18px; }
  .letterhead .footer {
    position: absolute; left: 52px; right: 52px; bottom: 48px;
    display: flex; justify-content: space-between; font-size: 5.5px; line-height: 1.5;
  }
  .footer-col { border-left: 3px solid var(--ink); padding-left: 5px; }

  /* Brand panel */
  .brand-panel {
    position: absolute; left: 0; top: 745px; width: 477px; height: 455px;
    background: var(--panel-white);
    display: flex; align-items: center; justify-content: center;
  }
  .brand-panel .brand-mark { font-size: 46px; gap: 16px; }
  .brand-panel .brand-mark .dot { width: 40px; height: 40px; }

  /* Card panel */
  .card-panel {
    position: absolute; left: 477px; top: 745px; width: 723px; height: 455px;
    background: var(--panel-dark);
  }
  .business-card {
    position: absolute; left: 82px; top: 78px; width: 560px; height: 300px;
    background: linear-gradient(135deg, var(--card), var(--card-dark));
    box-shadow: 0 8px 20px rgba(0,0,0,.35);
  }
  .business-card .rainbow-band { height: 14px; }
  .business-card .card-divider {
    position: absolute; left: 50%; top: 40px; bottom: 30px;
    border-left: 1px solid rgba(0,0,0,.35);
  }
  .business-card .brand-mark {
    position: absolute; left: 0; width: 50%; top: 130px; justify-content: center;
    font-size: 22px; color: #3a3f45;
  }
  .business-card .brand-mark .dot { width: 18px; height: 18px; background: #3a3f45; }
  .card-contact {
    position: absolute; left: calc(50% + 24px); top: 50px;
    color: var(--accent-yellow); font-size: 11px; line-height: 1.6;
  }
  .card-contact .person { font-size: 17px; font-weight: 700; line-height: 1.2; }
  .card-contact .role { margin-bottom: 22px; }
</style>
</head>
<body>

<section class="letterhead">
  <div class="rainbow-band"><span class="y"></span><span class="o"></span><span class="r"></span><span class="m"></span><span class="p"></span><span class="b"></span><span class="g"></span></div>
  <div class="sender-line">Name • Adresse 1 • Adresse 2</div>
  <div class="recipient">Max Mustermann<br>Straße<br>Ort</div>
  <div class="brand-mark"><span class="dot"></span>Velto Studio</div>

  <div class="letter-body">
    <p>Sehr geehrter Herr,</p>
    <p>Lorem ipsum dolor sit amet, consectetur adipiscing elit, sed do eiusmod tempor incididunt ut labore et dolore magna aliqua.</p>
    <p>Ut enim ad minim veniam, quis nostrud exercitation ullamco laboris nisi ut aliquip ex ea commodo consequat. Duis aute irure dolor in reprehenderit in voluptate velit esse cillum dolore eu fugiat nulla pariatur.</p>
    <p>Excepteur sint occaecat cupidatat non proident, sunt in culpa qui officia deserunt mollit anim id est laborum.</p>
    <p>Sed ut perspiciatis unde omnis iste natus error sit voluptatem accusantium doloremque laudantium, totam rem aperiam eaque ipsa quae ab illo inventore veritatis.</p>
    <p class="closing">Mit freundlichen Grüßen</p>
    <p class="signature">Name<br>Geschäftsführer</p>
  </div>

  <div class="footer">
    <div class="footer-col">Name<br>Adresse 1<br>Adresse 2</div>
    <div class="footer-col">Tel.: +49 (0) 123456<br>Fax: +49 (0) 123456<br>E-Mail: info@veltostudio.de</div>
    <div class="footer-col">Bankverbindung: xxxxxxxxx<br>IBAN: xxxxxxxxxxxxxxx<br>BIC: xxxxxxxxxxxxxx</div>
  </div>
</section>

<section class="brand-panel">
  <div class="brand-mark"><span class="dot"></span>Velto Studio</div>
</section>

<section class="card-panel">
  <div class="business-card">
    <div class="rainbow-band"><span class="y"></span><span class="o"></span><span class="r"></span><span class="m"></span><span class="p"></span><span class="b"></span><span class="g"></span></div>
    <div class="brand-mark"><span class="dot"></span>Velto Studio</div>
    <div class="card-divider"></div>
    <div class="card-contact">
      <div class="person">NAME NAME</div>
      <div class="role">Geschäftsführerin</div>
      <div>Adresse 1</div>
      <div>Adresse 2</div>
      <div>Tel.: 01234567</div>
      <div>info@veltostudio.de</div>
      <div>www.veltostudio.de</div>
    </div>
  </div>
</section>

</body>
</html>
```